Business Card for Jewelry Business

We need a new namecard design for a jewelry company based in Bangkok, Thailand. We have a new website recently and want the new namecard to reflect our new modern image. I have uploaded our old namecard to show you the information that needs to be on the namecard. Pls check our website www.qelburn.com for the new color scheme to help design the new namecard.

```html
<!DOCTYPE html>
<html lang="en">
<head>
<meta charset="utf-8">
<title>Qelburn Artisans – Business Card</title>
<link href="https://fonts.googleapis.com/css2?family=Montserrat:wght@400;500;600&display=swap" rel="stylesheet">
<style>
  :root {
    --backdrop: #2b2b2d;
    --card-dark: #1e1f21;
    --card-light: #ffffff;
    --ink: #111111;
    --teal: #6cc3c9;
    --sand: #e6ddd2;
    --white: #ffffff;
  }
  * { box-sizing: border-box; margin: 0; padding: 0; }
  html, body { width: 1200px; height: 1200px; overflow: hidden; }
  body {
    background: var(--backdrop);
    font-family: "Montserrat", sans-serif;
    display: flex;
    flex-direction: column;
    align-items: center;
    justify-content: center;
    gap: 36px;
  }
  .card {
    position: relative;
    width: 960px;
    height: 548px;
    border-bottom: 7px solid var(--teal);
    border-right: 4px solid var(--teal);
    overflow: hidden;
  }
  .card--front { background: var(--card-dark); }
  .card--back { background: var(--card-light); }

  .brand { position: absolute; text-align: center; font-family: "Montserrat", sans-serif; font-weight: 500; }
  .brand__name { display: block; letter-spacing: 0.06em; }
  .brand__sub { display: block; letter-spacing: 0.12em; }

  .card--front .brand { right: 70px; top: 205px; color: var(--white); }
  .card--front .brand__name { font-size: 64px; }
  .card--front .brand__sub { font-size: 20px; margin-top: 8px; }

  .card--back .brand { right: 60px; top: 150px; color: var(--ink); display: flex; align-items: center; gap: 22px; }
  .brand__dot { width: 28px; height: 28px; border-radius: 50%; background: var(--teal); flex: none; }
  .card--back .brand__name { font-size: 44px; }
  .card--back .brand__sub { font-size: 14px; margin-top: 6px; }

  .arc { position: absolute; left: 0; top: 0; }

  .contact { position: absolute; left: 110px; top: 150px; color: var(--ink); }
  .contact__name { font-size: 30px; font-weight: 600; letter-spacing: 0.02em; }
  .contact__role { font-size: 21px; color: var(--teal); margin-top: 2px; }
  .contact__list { list-style: none; margin-top: 18px; }
  .contact__item { display: flex; align-items: center; gap: 14px; font-size: 21px; line-height: 32px; }
  .contact__item svg { width: 20px; height: 20px; fill: var(--teal); flex: none; }
  .contact__address { font-size: 21px; line-height: 30px; margin-top: 26px; font-style: normal; }
</style>
</head>
<body>
  <section class="card card--front" aria-label="Card front">
    <div class="brand">
      <span class="brand__name">QELBURN</span>
      <span class="brand__sub">ARTISANS</span>
    </div>
  </section>

  <section class="card card--back" aria-label="Card back">
    <svg class="arc" width="960" height="548" viewBox="0 0 960 548" aria-hidden="true">
      <circle cx="320" cy="330" r="305" fill="none" stroke="var(--sand)" stroke-width="5"/>
    </svg>

    <div class="contact">
      <p class="contact__name">MALI TANASORN</p>
      <p class="contact__role">Sales &amp; Product Development Manager</p>
      <ul class="contact__list">
        <li class="contact__item">
          <svg viewBox="0 0 24 24"><path d="M6.6 10.8a15 15 0 0 0 6.6 6.6l2.2-2.2c.3-.3.7-.4 1-.2 1.1.4 2.3.6 3.6.6.6 0 1 .4 1 1V20c0 .6-.4 1-1 1A17 17 0 0 1 3 4c0-.6.4-1 1-1h3.5c.6 0 1 .4 1 1 0 1.3.2 2.5.6 3.6.1.3 0 .7-.2 1z"/></svg>
          +662-555-0147
        </li>
        <li class="contact__item">
          <svg viewBox="0 0 24 24"><path d="M7 3h10v5H7zM4 9h16a2 2 0 0 1 2 2v6h-4v4H6v-4H2v-6a2 2 0 0 1 2-2zm4 7v3h8v-3z"/></svg>
          +662-555-0182
        </li>
        <li class="contact__item">
          <svg viewBox="0 0 24 24"><path d="M2 5h20v14H2zm2 2v.5l8 5 8-5V7l-8 5z"/></svg>
          hello@qelburn.com
        </li>
        <li class="contact__item">
          <svg viewBox="0 0 24 24"><path d="M12 2a10 10 0 1 0 0 20 10 10 0 0 0 0-20zm-1 2.1V8H7.3A8 8 0 0 1 11 4.1zm2 0A8 8 0 0 1 16.7 8H13zM4.5 10H11v4H4.5a8 8 0 0 1 0-4zm8.5 0h6.5a8 8 0 0 1 0 4H13zM7.3 16H11v3.9A8 8 0 0 1 7.3 16zm5.7 0h3.7a8 8 0 0 1-3.7 3.9z"/></svg>
          www.qelburn.com
        </li>
      </ul>
      <address class="contact__address">
        48 Moo 7 Sukhon Road,<br>
        Nong Phai Industrial Park,<br>
        Bangkok, 10990 Thailand
      </address>
    </div>

    <div class="brand">
      <span class="brand__dot"></span>
      <span>
        <span class="brand__name">QELBURN</span>
        <span class="brand__sub">ARTISANS</span>
      </span>
    </div>
  </section>
</body>
</html>
```